Brolga Ridge Earthmoving & Transport Business Card

Can you please design a business card for an Earthworks, Haulage truck and machinery hire company. They also provide sand soil and mulch supply, as well as screening of products. Can you re-create the logo from the attached but add Brolga Ridge Earthmoving & Transport just use the three diamond design.

Target Market(s)

Earthmoving and Transport, Landscapers, Construction

Contact Information for Business Card

ABN 52 907 338 214, Dale Pettigrew, Managing Director, Brolga Ridge Earthmoving & Transport Mobile 0438 256 904 Email brgtransport2011@haulmail.example

Font styles to use
Sans Serif

Colors
ec1f27
000000
cbcbcb
ffffff

Requirements
Must have
• Listed on the back, Earthworks | Haulage | Truck and Machinery Hire | Sand, Soil & Mulch Supply | Screening of Products
Nice to have
• Would be good for it to look appealing to a mans man, because it relates to heavy machinery, earthworks, construction etc. Black, red and white would be good maybe with a bit of silver somewhere.
Should not have
• not sure

```html
<!DOCTYPE html>
<html lang="en">
<head>
<meta charset="utf-8">
<title>Brolga Ridge Earthmoving &amp; Transport – Business Card</title>
<link rel="stylesheet" href="https://fonts.googleapis.com/css2?family=Oswald:wght@600&family=Lato:wght@400&family=Tinos:wght@700&display=swap">
<style>
  :root {
    --red: #ec1f27;
    --black: #000000;
    --charcoal: #2e2e2e;
    --dark-band: #262626;
    --silver: #cbcbcb;
    --white: #ffffff;
    --ink: #1e1e1e;
    --stage: #e9e9e9;
  }
  * { margin: 0; padding: 0; box-sizing: border-box; }
  html, body { width: 1200px; height: 900px; overflow: hidden; }
  body {
    background: var(--stage);
    position: relative;
    font-family: "Lato", sans-serif;
  }
  .card {
    position: absolute;
    width: 600px;
    height: 366px;
    overflow: hidden;
    box-shadow: 0 6px 18px rgba(0,0,0,.18);
  }

  /* Brand face */
  .card--brand {
    left: 60px; top: 70px;
    background: var(--charcoal);
    display: flex; flex-direction: column; align-items: center; justify-content: center;
    gap: 14px;
  }
  .brand-mark { display: flex; align-items: center; gap: 16px; }
  .brand-mark__square { width: 46px; height: 46px; background: var(--red); }
  .brand-mark__name,
  .brand-tagline {
    font-family: "Oswald", sans-serif;
    font-weight: 600;
    color: var(--white);
    text-transform: uppercase;
    line-height: 1;
  }
  .brand-mark__name { font-size: 64px; letter-spacing: 6px; }
  .brand-tagline { font-size: 30px; letter-spacing: .5px; }
  .services {
    margin-top: 6px;
    padding-top: 12px;
    border-top: 1px solid var(--silver);
    width: 520px;
    text-align: center;
    font-size: 13px;
    line-height: 1.6;
    letter-spacing: .3px;
    color: var(--silver);
  }
  .services__line { display: block; white-space: nowrap; }

  /* Contact face */
  .card--contact {
    left: 540px; top: 464px;
    background: var(--white);
  }
  .swoosh { position: absolute; inset: 0; width: 100%; height: 100%; }
  .person { position: absolute; left: 44px; top: 48px; }
  .person__name {
    font-family: "Tinos", serif;
    font-weight: 700;
    font-size: 23px;
    color: var(--red);
    text-transform: uppercase;
    line-height: 1;
  }
  .person__role { font-size: 17px; color: var(--ink); margin-top: 3px; }

  .contact-mark {
    position: absolute; right: 40px; top: 50px;
    display: flex; align-items: center; gap: 12px;
  }
  .contact-mark__square { width: 30px; height: 30px; background: var(--red); }
  .contact-mark__name {
    font-family: "Lato", sans-serif;
    font-size: 44px; color: var(--ink); letter-spacing: 4px; line-height: 1;
  }

  .contact-list {
    position: absolute; left: 44px; top: 168px;
    list-style: none; font-size: 17px; color: var(--ink); line-height: 1.35;
  }
  .contact-list li { display: flex; align-items: center; gap: 8px; }
  .contact-list .icon { width: 14px; height: 14px; flex: none; fill: var(--red); }
  .contact-list .address { padding-left: 22px; }

  .abn {
    position: absolute; right: 30px; top: 256px;
    font-size: 13px; color: var(--white); letter-spacing: .3px;
  }
</style>
</head>
<body>

  <section class="card card--brand" aria-label="Business card, brand face">
    <div class="brand-mark">
      <span class="brand-mark__square"></span>
      <span class="brand-mark__name">BRG</span>
    </div>
    <p class="brand-tagline">Brolga Ridge Earthmoving &amp; Transport</p>
    <p class="services">
      <span class="services__line">Earthworks | Haulage | Truck and Machinery Hire</span>
      <span class="services__line">Sand, Soil &amp; Mulch Supply | Screening of Products</span>
    </p>
  </section>

  <section class="card card--contact" aria-label="Business card, contact face">
    <svg class="swoosh" viewBox="0 0 600 366" preserveAspectRatio="none" aria-hidden="true">
      <path fill="var(--red)" d="M0,296 C170,340 320,306 430,240 C505,196 560,184 600,184 L600,366 L0,366 Z"/>
      <path fill="var(--white)" d="M0,316 C170,352 325,318 438,250 C510,206 562,194 600,194 L600,366 L0,366 Z"/>
      <path fill="var(--dark-band)" d="M0,326 C170,358 330,326 446,256 C515,214 565,202 600,202 L600,366 L0,366 Z"/>
    </svg>

    <div class="person">
      <h1 class="person__name">Dale Pettigrew</h1>
      <p class="person__role">Managing Director</p>
    </div>

    <div class="contact-mark">
      <span class="contact-mark__square"></span>
      <span class="contact-mark__name">BRG</span>
    </div>

    <ul class="contact-list">
      <li>
        <svg class="icon" viewBox="0 0 16 16" aria-hidden="true"><path d="M3 2h3l1.5 3.5-2 1.2a8 8 0 0 0 3.8 3.8l1.2-2L14 10v3a1 1 0 0 1-1 1A11 11 0 0 1 2 3a1 1 0 0 1 1-1z"/></svg>
        <span>0438 256 904</span>
      </li>
      <li>
        <svg class="icon" viewBox="0 0 16 16" aria-hidden="true"><path d="M1 3h14v10H1z M1 3l7 6 7-6" stroke="var(--white)" stroke-width="1.2"/></svg>
        <span>brgtransport2011@haulmail.example</span>
      </li>
      <li class="address">48 Quarry Bend Hallorin 6099</li>
      <li class="address">Perth, WA</li>
    </ul>

    <p class="abn">ABN 52 907 338 214</p>
  </section>

</body>
</html>
```